Letterhead and Business Card for Wealth Management Company
Harborline Wealth Management
Letterhead and Business Card for Wealth Management Company - Financial Services
Creative Brief
Use same font as used in my logo
Can use the same font or add additional font
Professional
R. Dwight Voss, CRPC®
Wealth Advisor
2450 Fernbrook Avenue Suite 310 Ashcombe, PA 19455
dvoss@harborline-wealth.com
www.harborline-wealth.com
I work with affluent people so I want a sophisticated and classic looking business card and stationary. Our tagline is Grow. Keep. Thrive. with Live in italics. You can see it on our website at www.harborline-wealth.com. If appropriate, please include the tagline on the business card, letterhead and envelope. Please note the tagline on the website is a gradient color. It looks better printed in solid color.
Be creative.
dvoss dvoss
Thanks for all the great designs! I have a busy schedule today, but I will go through them and give star ratings later today or tonight. Thanks again!
Qwirk Qwirk

```html
<!DOCTYPE html>
<html lang="en">
<head>
<meta charset="utf-8">
<title>Harborline Wealth Management — Business Card</title>
<link href="https://fonts.googleapis.com/css2?family=Cormorant+Garamond:ital,wght@0,500;1,500&family=Open+Sans:wght@400;600&display=swap" rel="stylesheet">
<style>
  :root {
    --backdrop: #d9dadc;
    --card-white: #ffffff;
    --navy: #1f3f73;
    --name-blue: #2e5a94;
    --accent-orange: #e9a21e;
    --text-grey: #6b6f75;
    --tagline-white: #f3f5f9;
  }
  * { box-sizing: border-box; margin: 0; padding: 0; }
  html, body { width: 1200px; height: 778px; overflow: hidden; }
  body {
    background: var(--backdrop);
    font-family: "Open Sans", Arial, sans-serif;
    position: relative;
  }
  .card {
    position: absolute;
    width: 520px;
    height: 297px;
    box-shadow: 0 6px 18px rgba(0,0,0,0.25);
    overflow: hidden;
  }
  .card-front { left: 60px; top: 240px; background: var(--card-white); }
  .card-back { left: 620px; top: 240px; background: var(--navy); }

  .brand { position: absolute; display: flex; align-items: center; gap: 12px; }
  .brand-mark { width: 30px; height: 30px; background: var(--navy); flex: none; }
  .brand-name {
    font-family: "Cormorant Garamond", Georgia, serif;
    font-weight: 500;
    color: var(--navy);
    line-height: 1.05;
  }
  .card-front .brand { left: 30px; top: 34px; }
  .card-front .brand-name { font-size: 22px; width: 200px; }

  .person { position: absolute; left: 30px; top: 128px; }
  .person-name { font-size: 15px; color: var(--name-blue); letter-spacing: 0.2px; }
  .person-title { font-size: 8px; color: var(--accent-orange); margin-top: 1px; }

  .address {
    position: absolute; left: 30px; top: 170px;
    font-size: 10.5px; line-height: 15px; color: var(--text-grey);
    font-style: normal;
  }
  .contacts {
    position: absolute; left: 268px; top: 150px;
    list-style: none; font-size: 10.5px; line-height: 15px; color: var(--text-grey);
  }
  .contacts li { display: flex; align-items: center; gap: 6px; }
  .contacts svg { width: 10px; height: 10px; flex: none; }

  .web-url {
    position: absolute; right: 36px; bottom: 22px;
    font-size: 10.5px; color: var(--navy); font-weight: 600;
  }
  .front-band {
    position: absolute; right: 0; bottom: 0; width: 280px; height: 14px;
    background: var(--navy);
  }
  .front-band::before {
    content: ""; position: absolute; left: -14px; top: 0;
    border-right: 14px solid var(--navy); border-top: 14px solid transparent;
  }

  .card-back .brand { left: 92px; top: 92px; gap: 16px; }
  .card-back .brand-mark { width: 44px; height: 44px; background: var(--tagline-white); }
  .card-back .brand-name { color: var(--tagline-white); font-size: 30px; width: 320px; }
  .tagline {
    position: absolute; left: 150px; top: 200px;
    font-family: "Cormorant Garamond", Georgia, serif; font-weight: 500;
    font-size: 24px; color: var(--tagline-white); letter-spacing: 1px;
  }
  .tagline em { font-style: italic; }
</style>
</head>
<body>
  <section class="card card-front">
    <div class="brand">
      <span class="brand-mark"></span>
      <span class="brand-name">Harborline Wealth Management</span>
    </div>
    <div class="person">
      <p class="person-name">R. Dwight Voss, CRPC®</p>
      <p class="person-title">Wealth Advisor</p>
    </div>
    <address class="address">
      2450 Fernbrook Avenue<br>Suite 310<br>Ashcombe, PA 19455
    </address>
    <ul class="contacts">
      <li><svg viewBox="0 0 10 10"><rect x="0" y="3" width="10" height="6" rx="1" fill="#e9a21e"/><rect x="2" y="1" width="6" height="3" rx="1" fill="#e9a21e"/></svg>555-014-2730</li>
      <li><svg viewBox="0 0 10 10"><rect x="2.5" y="0" width="5" height="10" rx="1" fill="#e9a21e"/></svg>555-014-8862</li>
      <li><svg viewBox="0 0 10 10"><rect x="0" y="4" width="10" height="5" rx="1" fill="#e9a21e"/><rect x="2" y="0" width="6" height="5" fill="#e9a21e"/></svg>555-014-2795</li>
      <li><svg viewBox="0 0 10 10"><rect x="0" y="1.5" width="10" height="7" rx="1" fill="#e9a21e"/><path d="M0.5 2 L5 6 L9.5 2" stroke="#fff" fill="none" stroke-width="1"/></svg>dvoss@harborline-wealth.com</li>
    </ul>
    <p class="web-url">www.harborline-wealth.com</p>
    <div class="front-band"></div>
  </section>

  <section class="card card-back">
    <div class="brand">
      <span class="brand-mark"></span>
      <span class="brand-name">Harborline Wealth Management</span>
    </div>
    <p class="tagline">Grow. Keep. <em>Thrive.</em></p>
  </section>
</body>
</html>
```